www.veloramirel.net

Hi,
UPDATE: Logo attached
TAG LINE NEW: OBITUARIES * CONDOLENCE NOTES
MULTIMEDIA MEMORIAL
Please refer to our existing site for more explanation of who we are?
We are a global data collecting portal site managing the Jewish funeral industry where users:
a) family and freinds in grief or "ancestry" searching persons
b) chevra kadisha's (funeral parlor)
c) current and historic cemetaries
d) Jewish Media Partners
arrive and choose a function (category):
in order to:
- upload a basic listing (FREE)
- upload/upgrade a multimedia listing (PAID)
- or search for a listing
of a deceased person (potentially millions of entries)
The functions (or categories) are accessed after the user:
Chooses their global location of search by
"Choose your Location" ie: Australia/NZ (which country?)
and allows the USER to choose a category function such as:
GROUP A (Local Info) GROUP B (Soul Search)
Chevra Kadisha Funerals (within 7 days)
Cemetaries Recently Deceased (up to 12mth)
Stonemasons Soul Search (after 1 year)
Jewish Media Partners
GROUP C (Jewish Death & Mourning Customs)
The way of Jewish burial
3000 y/old customs
When will Moshiach Come ?
Will I see my loved one again?
AIM:
To utilize existing logo and side menus (Member, Main & Resources) to create a user freindly and simpler friendly landing page, warmer and more softer for viewers.
To create logo buttons for the service catogories:
A, B & C and separate sub catagories
The MAIN AIM is to offer users opportunity to upload (LOG-IN required)
a) NEW basic FREE listing
b) NEW Multi-media PAID listing
SUMMARY:
1) User arrives at landing paid and sees global map, where he/she must choose the location in order to localize his data search
At this point, he/she can see what the site offers by the side MAIN, menu and icon function/catagories
(ie: Soul Search, New Basic Listing, Multimedia Listing)
2) After arriving at location (ie: Australia/NZ), the user then chooses the sub-function icon:
A- Local Funeral Service Info (Chevra Kadisha, Cemetary etc)
B- Soul Search (Funeral,Recently Deceased, Soul Search)
C- Jewish Death & Mourning Cutoms
Hi
Reason: Because of the holidays, we are happy to extend the deadline....
happy times
Target Market(s)
Family persons (Guest Member) & Industry (Members)
Industry/Entity Type
Industry
Requirements
Must have
- Style : Simple, Neat & Easy to Navigate
Icons: for each catagory/function
Colors; natural
-
Ability to bring inspiration, hope, light and healing to a difficult subject matter. (site look)
-
Education a profoundly deep 3000 y/old historically rich and mystic tradition to a wide audience
-
Allow children to access and upload data about grandparents etc
-
To promote on landing page the Invitation of local Chevra Kadisha's (funeral parlors), who have no web exposure, to get involved and LOG-IN and upload basic or multimedia listings.
(ie: please Register your local Chevra Kadisha here)
-
To promote on the landing page sample listings (Recently Deceased), to show look/feel of listings

```html
<!DOCTYPE html>
<html lang="en">
<head>
<meta charset="utf-8">
<title>Veloramirel.net — Global Chevra Kadisha Network</title>
<link href="https://fonts.googleapis.com/css2?family=Sorts+Mill+Goudy&family=Open+Sans:wght@400;600&display=swap" rel="stylesheet">
<style>
:root{
  --ink:#2b2b2b;
  --text:#333;
  --muted:#777;
  --orange:#f29a1f;
  --orange-dark:#c9700c;
  --panel:#e6e6e6;
  --panel-line:#cfcfcf;
  --nav:#e9e9e9;
  --dropdown:#6d6d6d;
  --hero-a:#8a5a2e;
  --hero-b:#e8d6b8;
  --brown:#8a4a12;
  --white:#fff;
}
*{box-sizing:border-box;margin:0;padding:0}
html,body{width:754px;height:1200px;overflow:hidden;background:var(--white)}
body{position:relative;font-family:"Open Sans",Arial,sans-serif;color:var(--text)}
.abs{position:absolute}

/* header */
.brand{left:36px;top:58px;font-family:"Sorts Mill Goudy",Georgia,serif;font-size:20px;color:var(--ink);display:flex;align-items:center;gap:8px}
.brand-dot{width:12px;height:12px;border-radius:50%;background:var(--orange)}
.region-prompt{left:312px;top:2px;font-size:9px;color:var(--orange-dark)}
.world-map{left:232px;top:14px;width:228px;height:104px;background:linear-gradient(#e4e4e4,#d2d2d2);border-radius:40px 30px 50px 30px}
.region-box{left:555px;top:0;width:177px;height:57px;background:linear-gradient(#f1f1f1,#dcdcdc);border:1px solid #cfcfcf;border-top:none;border-radius:0 0 4px 4px}
.region-row{position:absolute;left:12px;font-size:10px;color:#444;display:flex;align-items:center}
.region-row span{width:46px}
.select{width:108px;height:17px;border-radius:9px;background:linear-gradient(#fff,#e6e6e6);border:1px solid #bbb;font-size:10px;padding-left:8px;line-height:15px;position:relative;color:#111}
.select:after{content:"";position:absolute;right:10px;top:6px;border:4px solid transparent;border-top:5px solid #333}
.translate-box{left:519px;top:62px;width:213px;height:56px;border:1px solid #cfcfcf;border-radius:4px;background:linear-gradient(#fbfbfb,#ececec)}
.translate-select{position:absolute;left:10px;top:7px;width:192px;height:20px;background:#fff;border:1px solid #ccc;font-size:9px;color:#888;padding:3px 8px}
.translate-credit{position:absolute;left:27px;top:34px;font-size:9.5px;color:#444}
.translate-credit b{font-size:14px;font-weight:600;color:#555}

/* nav */
.main-nav{left:0;top:122px;width:754px;height:26px;background:linear-gradient(#f4f4f4,#dedede);border-top:1px solid #d5d5d5;border-bottom:1px solid #cfcfcf}
.main-nav ul{list-style:none;display:flex;margin-left:28px;height:100%;align-items:center;font-family:"Sorts Mill Goudy",Georgia,serif;font-size:13.5px;color:#444;white-space:nowrap}
.main-nav li{padding:0 6px;margin-right:6px;line-height:25px}
.main-nav li.active{background:linear-gradient(#f8c36a,#f29a1f);color:#5a2d00;padding:0 9px;margin-right:4px}
.submenu{left:28px;top:148px;width:108px;height:134px;background:linear-gradient(#747474,#5e5e5e);opacity:.94;padding-top:6px;z-index:3}
.submenu li{list-style:none;color:#fff;font-size:9.5px;height:22.6px;line-height:22px;padding-left:18px;white-space:nowrap}
.submenu li:first-child{background:#4e4e4e}

/* hero */
.hero-shadow{left:10px;top:150px;width:734px;height:245px;background:linear-gradient(90deg,#d8d8d8,#f4f4f4 8%,#f4f4f4 92%,#d8d8d8)}
.hero{left:25px;top:155px;width:703px;height:207px;background:radial-gradient(ellipse at 55% 40%,#c77a3a 0%,var(--hero-a) 35%,var(--hero-b) 80%)}
.hero-arrow{top:250px;width:28px;height:28px;border-radius:4px;background:linear-gradient(#b06a24,#7d4513);z-index:4}
.hero-arrow svg{display:block;margin:7px auto}
.hero-caption{left:25px;top:362px;width:703px;height:28px;background:#fff;text-align:center;font-family:"Sorts Mill Goudy",Georgia,serif;font-size:16px;line-height:30px;color:#2d2d2d}

/* partners */
.partners{left:0;top:405px;width:754px;height:42px}
.partner{position:absolute;top:4px;height:30px;background:#c9c9c9;border-radius:2px}
.strip-line{left:0;top:455px;width:754px;height:1px;background:#e0e0e0}

/* content */
.section-title{font-family:"Sorts Mill Goudy",Georgia,serif;font-weight:400;font-size:18.5px;color:#2b2b2b;white-space:nowrap}
.body-copy{font-size:8.9px;line-height:13.4px;color:#3a3a3a;text-align:justify}
.body-copy p{margin-bottom:13px}
.region-shape{float:left;width:88px;height:66px;margin:0 6px 2px 0;background:#8e8e8e;border-radius:30% 45% 40% 35%}
.read-more{width:62px;height:17px;border-radius:4px;background:linear-gradient(#ececec,#d0d0d0);font-size:9px;color:#666;text-align:center;line-height:17px;white-space:nowrap}
.global-search{left:207px;top:462px;width:111px;height:43px;border:1px solid #ccc;border-radius:3px;background:linear-gradient(#fff,#e4e4e4)}
.global-search .label{position:absolute;left:0;width:100%;top:1px;text-align:center;font-family:"Sorts Mill Goudy",Georgia,serif;font-size:10.5px;color:#444}
.gs-icon{position:absolute;top:18px;width:20px;height:20px;border-radius:50%;background:radial-gradient(#fff,#b8b8b8);border:1px solid #999}
.ask-rabbi{left:319px;top:462px;width:167px;height:43px;border:1px solid #ccc;border-radius:3px;background:linear-gradient(#fafafa,#e4e4e4);font-family:"Sorts Mill Goudy",Georgia,serif;font-size:18px;color:#2b2b2b;overflow:hidden}
.ask-rabbi svg{position:absolute;left:8px;top:8px}
.ask-rabbi span{position:absolute;left:40px;top:11px;white-space:nowrap;line-height:22px}

/* sidebar */
.card{background:linear-gradient(#f3f3f3,#e2e2e2);border:1px solid var(--panel-line);border-radius:4px}
.card-tab{position:absolute;left:12px;right:12px;top:-1px;height:27px;background:linear-gradient(#fafafa,#d9d9d9);border-radius:0 0 3px 3px;text-align:center;font-family:"Sorts Mill Goudy",Georgia,serif;font-size:16px;line-height:27px;color:#333;box-shadow:0 2px 2px rgba(0,0,0,.12);white-space:nowrap}
.card-text{position:absolute;font-size:8.8px;line-height:13px;color:#222}
.card-icon{position:absolute;border-radius:6px}
.cta{position:absolute;height:17px;border-radius:3px;background:linear-gradient(#fbb74a,#f08c12);border:1px solid #c87010;font-size:10.5px;color:#3a1d00;text-align:center;line-height:15px;white-space:nowrap}
.passing{position:absolute;left:10px;width:190px;height:76px}
.passing h4{font-weight:400;font-size:12.5px;color:#333;white-space:nowrap}
.passing p{font-size:8.2px;line-height:13px;color:#444;width:108px;margin-top:4px}
.passing .photo{position:absolute;left:114px;top:-2px;width:64px;height:52px}
.passing .tag{position:absolute;left:106px;top:55px;font-size:9.3px;color:#333;white-space:nowrap}
.field{position:absolute;left:19px;width:172px;height:21px;background:#fff;border:1px solid #ddd;border-radius:5px;font-size:9.5px;color:#aaa;padding:3px 12px}

/* footer */
.footer-line{left:0;top:1155px;width:754px;height:1px;background:#ddd}
.copyright{left:9px;top:1164px;font-size:9px;color:#888}
.social{top:1162px;width:16px;height:16px;border-radius:2px;background:#7a8da8}
</style>
</head>
<body>

<header>
  <div class="abs brand"><span class="brand-dot"></span>Veloramirel.net</div>
  <div class="abs region-prompt">Please Choose your Region</div>
  <div class="abs world-map" role="img" aria-label="Grey world map for choosing a region"></div>
  <div class="abs region-box">
    <div class="region-row" style="top:7px"><span>Region :</span><div class="select">Israel</div></div>
    <div class="region-row" style="top:31px"><span>State:</span><div class="select">Israel</div></div>
  </div>
  <div class="abs translate-box">
    <div class="translate-select">Select Language</div>
    <div class="translate-credit">Powered by <b>Lumo</b> Translate</div>
  </div>
</header>

<nav class="abs main-nav">
  <ul>
    <li class="active">Home</li><li>Local Info</li><li>Recent Passings</li><li>Jewish Mysticism</li><li>Resources</li><li>SoulPage</li><li>Admin</li>
  </ul>
</nav>

<div class="abs hero-shadow"></div>
<div class="abs hero" role="img" aria-label="Close-up of a bronze Star of David resting on an open page of Hebrew text"></div>
<ul class="abs submenu">
  <li>Our mission</li><li>About Us</li><li>Personal Media</li><li>Contact Us</li><li>On-line Forum</li>
</ul>
<div class="abs hero-arrow" style="left:20px"><svg width="12" height="14"><path d="M11 1 L2 7 L11 13Z" fill="#fff" opacity=".5"/></svg></div>
<div class="abs hero-arrow" style="left:706px"><svg width="12" height="14"><path d="M1 1 L10 7 L1 13Z" fill="#fff"/></svg></div>
<div class="abs hero-caption">Welcome to the global Chevra Kadisha network</div>

<div class="abs partners" aria-label="Media partners">
  <svg class="abs" style="left:40px;top:14px" width="8" height="10"><path d="M7 0 L0 5 L7 10Z" fill="#aaa"/></svg>
  <div class="partner" style="left:67px;width:34px"></div>
  <div class="partner" style="left:132px;width:104px"></div>
  <div class="partner" style="left:258px;width:140px;height:22px;top:8px"></div>
  <div class="partner" style="left:418px;width:124px;height:22px;top:8px"></div>
  <div class="partner" style="left:556px;width:136px"></div>
  <svg class="abs" style="left:712px;top:14px" width="8" height="10"><path d="M0 0 L7 5 L0 10Z" fill="#aaa"/></svg>
</div>
<div class="abs strip-line"></div>

<main>
  <h2 class="abs section-title" style="left:31px;top:467px">Choose Your Region</h2>
  <div class="abs global-search">
    <div class="label">Global Search</div>
    <div class="gs-icon" style="left:14px"></div>
    <div class="gs-icon" style="left:44px"></div>
    <div class="gs-icon" style="left:75px"></div>
  </div>
  <div class="abs ask-rabbi">
    <svg width="26" height="26"><circle cx="13" cy="13" r="12" fill="#5aa83a"/><text x="13" y="19" text-anchor="middle" font-family="Arial" font-weight="bold" font-size="17" fill="#fff">?</text></svg>
    <span>Ask the Rabbi?</span>
  </div>

  <div class="abs body-copy" style="left:30px;top:514px;width:455px">
    <p><span class="region-shape" role="img" aria-label="Grey outline map of Australia"></span>Contrary to popular belief, Lorem Ipsum is not simply random text. It has roots in a piece of classical Latin literature from 45 BC, making it over 2000 years old. Edwin Harlow, a Latin professor at Marrow Hill College in Virginia, looked up one of the more obscure Latin words, consectetur, from a Lorem Ipsum passage, and going through the cites of the word in classical literature, discovered the undoubtable source. Lorem Ipsum comes from sections 1.10.32 and 1.10.33 of "de Finibus Bonorum et Malorum" (The Extremes of Good and Evil) by Varenus, written in 45 BC. This book is a treatise on the theory of ethics, very popular during the Renaissance. Contrary to popular belief, Lorem Ipsum is not simply random text. It has roots in a piece of classical Latin literature from 45 BC, making it over 2000 years old.</p>
    <p>Edwin Harlow, a Latin professor at Marrow Hill College in Virginia, looked up one of the more obscure Latin words, consectetur, from a Lorem Ipsum passage, and going through the cites of the word in classical literature, discovered the undoubtable source. Lorem Ipsum comes from sections 1.10.32 and 1.10.33 of "de Finibus Bonorum et Malorum" (The Extremes of Good and Evil) by Varenus, written in 45 BC. This book is a treatise on the theory of ethics, very popular during the Renaissance. Contrary to popular belief, Lorem Ipsum is not simply random text. It has roots in a piece of classical Latin literature from 45 BC, making it over 2000 years old. Edwin Harlow, a Latin professor at Marrow Hill College in Virginia, looked up one of the more obscure Latin words, consectetur, from a Lorem Ipsum passage, and going through the cites of the word in classical literature, discovered the undoubtable source.</p>
  </div>
  <div class="abs read-more" style="left:418px;top:789px">Read more...</div>

  <h2 class="abs section-title" style="left:28px;top:819px">Sub Heading</h2>
  <div class="abs body-copy" style="left:30px;top:851px;width:455px">
    <p>comes from sections 1.10.32 and 1.10.33 of "de Finibus Bonorum et Malorum" (The Extremes of Good and Evil) by Varenus, written in 45 BC. This book is a treatise on the theory of ethics, very popular during the Renaissance. Contrary to popular belief, Lorem Ipsum is not simply random text. It has roots in a piece of classical Latin literature from 45 BC, making it over 2000 years old.</p>
    <p>Edwin Harlow, a Latin professor at Marrow Hill College in Virginia, looked up one of the more obscure Latin words, consectetur, from a Lorem Ipsum passage, and going through the cites of the word in classical literature, discovered the undoubtable source. Lorem Ipsum comes from sections 1.10.32 and 1.10.33 of "de Finibus Bonorum et Malorum" (The Extremes of Good and Evil) by Varenus, written in 45 BC. This book is a treatise on the theory of ethics, very popular during the Renaissance. Contrary to popular belief, Lorem Ipsum is not simply random text. It has roots in a piece of classical Latin literature from 45 BC, making it over 2000 years old. Edwin Harlow, a Latin professor at Marrow Hill College in Virginia, looked up one of the more obscure Latin words, consectetur, from a Lorem Ipsum passage, and going through the cites of the word in classical literature, discovered the undoubtable source.</p>
  </div>
  <div class="abs read-more" style="left:418px;top:1056px">Read more...</div>
</main>

<aside>
  <section class="abs card" style="left:520px;top:460px;width:213px;height:126px">
    <div class="card-tab">Online Obituary</div>
    <div class="card-icon" style="left:11px;top:42px;width:36px;height:46px;background:linear-gradient(#9a9a9a,#4a4a4a)" role="img" aria-label="Small illustration of a man in a suit"></div>
    <div class="card-text" style="left:55px;top:36px;width:156px">Lorem Ipsum is simply dummy text of the printing and typesetting industry. Lorem Ipsum has been the industry's standard dummy text ever</div>
    <div class="cta" style="left:59px;top:97px;width:111px">RECORD HERE</div>
  </section>

  <section class="abs card" style="left:520px;top:593px;width:213px;height:100px">
    <div class="card-tab">Condolence Comment</div>
    <div class="card-icon" style="left:11px;top:30px;width:40px;height:44px;background:linear-gradient(#e4b36b,#6f9a4a)" role="img" aria-label="Small illustration of two people together"></div>
    <div class="card-text" style="left:56px;top:27px;width:152px">Lorem Ipsum is simply dummy text of the printing and typesetting industry.</div>
    <div class="cta" style="left:51px;top:75px;width:108px">SEND HERE</div>
  </section>

  <section class="abs card" style="left:520px;top:700px;width:213px;height:104px">
    <div class="card-tab">Memorial Soulpage</div>
    <div class="card-icon" style="left:9px;top:32px;width:36px;height:42px;background:linear-gradient(#e44a3a,#7a1a12 70%,#3d6b2a)" role="img" aria-label="Small illustration of a memorial candle"></div>
    <div class="card-text" style="left:62px;top:29px;width:148px">Lorem Ipsum is simply dummy text of the printing and typesetting industry.</div>
    <div class="cta" style="left:51px;top:74px;width:108px">CREATE HERE</div>
  </section>

  <section class="abs card" style="left:522px;top:810px;width:211px;height:185px">
    <div class="card-tab">Recent Passings</div>
    <div class="passing" style="top:30px">
      <h4>Daniel Ashford</h4>
      <p>Lorem Ipsum is simply dummy text of the printing and typesetting industry.</p>
      <div class="photo" role="img" aria-label="Photo of an older woman with a younger relative" style="background:linear-gradient(#c8b8a6,#8a7a6c)"></div>
      <div class="tag">Recently Deceased</div>
    </div>
    <div class="abs" style="left:10px;top:104px;width:190px;height:1px;background:#c9c9c9"></div>
    <div class="passing" style="top:108px">
      <h4>Daniel Ashford</h4>
      <p>Lorem Ipsum is simply dummy text of the printing and typesetting industry.</p>
      <div class="photo" role="img" aria-label="Photo of footprints in sand" style="background:linear-gradient(#d9b98a,#8f6a3a)"></div>
      <div class="tag">Recently Deceased</div>
    </div>
  </section>

  <section class="abs card" style="left:520px;top:1005px;width:213px;height:128px">
    <div class="card-tab">Login</div>
    <div class="field" style="top:33px">User name</div>
    <div class="field" style="top:64px">Password</div>
    <div class="cta" style="left:77px;top:95px;width:59px">Login</div>
  </section>
</aside>

<footer>
  <div class="abs footer-line"></div>
  <div class="abs copyright">Copyright © 2011. www.veloramirel.net</div>
  <div class="abs social" style="left:602px"></div>
  <div class="abs social" style="left:627px"></div>
  <div class="abs social" style="left:651px"></div>
  <div class="abs social" style="left:675px"></div>
  <div class="abs social" style="left:698px"></div>
</footer>

</body>
</html>
```